Wildlife photographer Website

The website is to be a "resume" of pictures and awards won by Nora. Lean heavy to outdoor wildlife.
She will post articles and have ability to interact with fans.

I will add some of her pictures tonight,

Target Market(s)

Terra Quarterly .....anyone looking to hire a wildlife photographer.

Industry/Entity Type

Professional Photography

Contact Information for Business Card

Nora Falkett
4817 Maple Hollow Lane
Columbia MD 21078
443-581-2094
Nora@FernOwlPix.com

Coding

Coded - Design and coding required

Number of Pages Required

5+ page

Requirements
Must have
• New Logo
Nice to have
• Nature, and eye catching graphics

```html
<!DOCTYPE html>
<html lang="en">
<head>
<meta charset="utf-8">
<title>Wild Nora — Nora Falkett</title>
<link href="https://fonts.googleapis.com/css2?family=Anton&family=Open+Sans:wght@400;600;700&display=swap" rel="stylesheet">
<style>
  :root{
    --ink:#111111;
    --black:#0b0b0b;
    --white:#ffffff;
    --paper:#ffffff;
    --muted:#6b6b6b;
    --soft:#bdbdbd;
    --line:#2a2a2a;
    --heading:"Anton", "Oswald", sans-serif;
    --body:"Open Sans", Arial, sans-serif;
  }
  *{box-sizing:border-box;margin:0;padding:0}
  html,body{width:1200px;height:3000px;overflow:hidden;background:var(--paper)}
  body{font-family:var(--body);color:var(--ink)}
  .page{width:1200px;height:3000px;display:flex;flex-direction:column}

  /* hero */
  .hero{position:relative;height:360px;overflow:hidden;
    background:
      radial-gradient(ellipse 260px 200px at 560px 40px, rgba(230,225,190,.75), rgba(120,130,90,.25) 60%, transparent 80%),
      radial-gradient(ellipse 200px 150px at 600px 220px, #4a4537, transparent 75%),
      linear-gradient(90deg,#12201a 0%,#1f3326 30%,#3b4a35 50%,#1e3024 72%,#0f1b15 100%);}
  .hero-photo{position:absolute;inset:0}
  .nav{position:absolute;top:0;left:0;right:0;height:60px;display:flex;align-items:center;justify-content:space-between;padding:0 60px}
  .brand{font-family:var(--heading);color:var(--white);font-size:15px;letter-spacing:1px}
  .menu-icon{width:22px;height:16px}
  .hero-name{position:absolute;left:0;right:0;top:190px;text-align:center;
    font-family:var(--body);font-weight:700;color:var(--white);font-size:64px;letter-spacing:6px;line-height:1}

  /* about */
  .about{height:240px;display:flex;align-items:center;gap:56px;padding:0 230px}
  .about-photo{width:180px;height:170px;flex:none;background:linear-gradient(160deg,#6c8a74,#2e6f8a 55%,#c2452f)}
  .about h2{font-family:var(--heading);font-size:30px;letter-spacing:1px;margin-bottom:12px}
  .about p{font-size:12px;line-height:1.7;color:var(--muted);max-width:480px;margin-bottom:18px}
  .btn{display:inline-block;background:var(--black);color:var(--white);font-size:11px;font-weight:600;padding:10px 20px}
  .btn-light{background:var(--white);color:var(--ink)}

  /* feature split rows */
  .split{height:300px;display:flex;background:var(--black);color:var(--white)}
  .split-text{width:600px;padding:54px 60px 0 60px}
  .split-right .split-text{padding-left:40px}
  .eyebrow{font-size:10px;font-weight:700;letter-spacing:1px;text-transform:uppercase;margin-bottom:6px}
  .split h3{font-family:var(--heading);font-size:34px;letter-spacing:1px;margin-bottom:14px}
  .split p{font-size:12px;line-height:1.75;color:var(--soft);max-width:470px;margin-bottom:22px}
  .split-photo{width:600px;height:300px}
  .photo-duck{background:linear-gradient(180deg,#8fb2c9 0%,#4f7ea3 55%,#26506f 100%)}
  .photo-fox{background:radial-gradient(ellipse at 55% 50%,#c0612a,#7a4a2a 45%,#3d3b24 80%)}

  /* exclusive */
  .exclusive{height:560px;padding-top:62px;text-align:center}
  .section-title{font-family:var(--heading);font-size:34px;letter-spacing:1px;margin-bottom:10px}
  .section-sub{font-size:12px;line-height:1.6;color:var(--muted);max-width:440px;margin:0 auto}
  .cards{display:flex;justify-content:center;gap:52px;margin-top:42px}
  .card{width:232px;text-align:center}
  .card-photo{width:232px;height:190px;margin-bottom:18px}
  .card h4{font-size:11px;font-weight:700;text-transform:uppercase;margin-bottom:8px}
  .card p{font-size:11px;line-height:1.6;color:var(--muted);margin-bottom:12px;min-height:53px}
  .card .more{font-size:11px;font-weight:600;border-bottom:1px solid var(--ink);padding-bottom:1px}
  .p-water{background:linear-gradient(180deg,#3f6f9a,#a7b9c4 55%,#2c5a84)}
  .p-wing{background:linear-gradient(160deg,#9ca67c,#7e6040 55%,#b8b090)}
  .p-bird{background:linear-gradient(180deg,#d9c8a6,#c7a87a 60%,#8c9aa0)}

  /* conservation banner */
  .banner{position:relative;height:380px;display:flex;align-items:center;justify-content:center;
    background:radial-gradient(ellipse at 30% 40%,#d8c7a8,#a88a64 60%,#7c6344)}
  .banner-box{position:relative;width:560px;height:220px;border:2px solid rgba(255,255,255,.85);background:rgba(255,255,255,.28);
    display:flex;flex-direction:column;align-items:center;justify-content:center;text-align:center}
  .banner-box h2{font-family:var(--heading);font-size:30px;line-height:1.2;letter-spacing:1px;color:var(--ink);margin-bottom:22px}

  /* articles */
  .articles{height:520px;padding-top:52px;text-align:center}
  .articles .card-photo{height:170px}
  .articles .card h4{margin-bottom:4px}
  .articles .card p{min-height:35px}
  .date{font-size:10px;color:var(--muted)}
  .p-otter{background:linear-gradient(170deg,#6e7a3e,#8a6a3c 55%,#3d4a2a)}
  .p-flock{background:linear-gradient(180deg,#b9b7a4,#8a8a70 60%,#5f6552)}
  .p-ducks{background:linear-gradient(180deg,#2d5f8c,#4e82ad 60%,#1f4769)}

  /* footer */
  .footer{height:340px;background:var(--black);color:var(--white);padding:56px 60px 0 60px;position:relative}
  .footer-cols{display:flex;gap:70px}
  .footer-col h5{font-family:var(--heading);font-size:15px;letter-spacing:1px;margin-bottom:18px}
  .footer-about{width:270px}
  .footer-about p{font-size:11px;line-height:1.7;color:var(--soft);margin-bottom:18px}
  .social{display:flex;gap:10px}
  .social span{width:18px;height:18px;border-radius:50%;border:1px solid var(--soft)}
  .footer ul{list-style:none}
  .footer li{font-size:11px;color:var(--soft);margin-bottom:11px;display:flex;align-items:center;gap:8px}
  .footer li::before{content:"";width:4px;height:4px;background:var(--soft);border-radius:50%;flex:none}
  .footer .contact li::before{display:none}
  .footer .contact svg{width:12px;height:12px;flex:none}
  .footer-col.links{width:170px}
  .copyright{position:absolute;left:60px;right:60px;bottom:26px;border-top:1px solid var(--line);padding-top:16px;text-align:center;font-size:10px;color:var(--soft)}
</style>
</head>
<body>
<div class="page">

  <header class="hero">
    <div class="hero-photo" role="img" aria-label="Elephant walking through a misty forest lit by a beam of sunlight"></div>
    <nav class="nav">
      <span class="brand">WILD NORA</span>
      <svg class="menu-icon" viewBox="0 0 22 16"><rect y="0" width="22" height="2" fill="#fff"/><rect y="7" width="22" height="2" fill="#fff"/><rect y="14" width="22" height="2" fill="#fff"/></svg>
    </nav>
    <h1 class="hero-name">WILD NORA</h1>
  </header>

  <section class="about">
    <div class="about-photo" role="img" aria-label="Portrait of the photographer outdoors in a red jacket"></div>
    <div>
      <h2>BY NORA. FALKETT</h2>
      <p>Wildlife photographer based in Maryland, chasing light across forests, wetlands and open plains. Every frame is made in the field with patience, respect for the animals and an eye for quiet, honest moments in nature that deserve to be seen.</p>
      <span class="btn">Learn More</span>
    </div>
  </section>

  <section class="split">
    <div class="split-text">
      <div class="eyebrow">Capturing wild moments</div>
      <h3>LOREM IPSUM</h3>
      <p>From frozen lakes to coastal marshes, each trip is planned around the seasons and the habits of the animals. Long mornings in a blind and slow walks at dusk bring the images that tell their stories best.</p>
      <span class="btn btn-light">Read More</span>
    </div>
    <div class="split-photo photo-duck" role="img" aria-label="Long-tailed duck swimming on blue water"></div>
  </section>

  <section class="split split-right">
    <div class="split-photo photo-fox" role="img" aria-label="Red fox resting among autumn leaves"></div>
    <div class="split-text">
      <div class="eyebrow">Nature in focus</div>
      <h3>LOREM IPSUM</h3>
      <p>Quiet woodland edges are home to foxes, deer and owls. Working with natural light and a respectful distance keeps every animal at ease and lets its true character show through in the final photograph.</p>
      <span class="btn btn-light">Read More</span>
    </div>
  </section>

  <section class="exclusive">
    <h2 class="section-title">WILD'S EXCLUSIVE | JUST FOR YOU!</h2>
    <p class="section-sub">Fresh stories from the field, hand picked from recent trips and shared first with our wildlife community.</p>
    <div class="cards">
      <article class="card">
        <div class="card-photo p-water" role="img" aria-label="Bird skimming across rippled water"></div>
        <h4>Wild creatures in the field</h4>
        <p>Notes and frames from a cold morning on the bay, waiting for the flock to lift off the water.</p>
        <span class="more">Read More</span>
      </article>
      <article class="card">
        <div class="card-photo p-wing" role="img" aria-label="Duck stretching its wings in a marsh"></div>
        <h4>Wild creatures in the field</h4>
        <p>A patient afternoon in the reeds brings a rare glimpse of a duck spreading its wings wide.</p>
        <span class="more">Read More</span>
      </article>
      <article class="card">
        <div class="card-photo p-bird" role="img" aria-label="Small shorebird standing on sand"></div>
        <h4>Wild creatures in the field</h4>
        <p>Shorebirds along the tideline move fast, so every shot is a small lesson in timing and calm.</p>
        <span class="more">Read More</span>
      </article>
    </div>
  </section>

  <section class="banner" role="img" aria-label="Close-up of a sandy owl feather texture behind the message">
    <div class="banner-box">
      <h2>WE CONTRIBUTE TO WILDLIFE<br>CONSERVATION THROUGH WILDLIFE<br>PHOTOGRAPHY</h2>
      <span class="btn">Contact Us</span>
    </div>
  </section>

  <section class="articles">
    <h2 class="section-title">WILD ARTICLE</h2>
    <p class="section-sub">Field notes, gear tips and stories behind the images, written for anyone who loves wildlife photography.</p>
    <div class="cards">
      <article class="card">
        <div class="card-photo p-otter" role="img" aria-label="Otter on a grassy riverbank"></div>
        <h4>Wildlife Photography</h4>
        <p>Tracking river otters at first light along a quiet creek.</p>
        <div class="date">June 4, 2024</div>
      </article>
      <article class="card">
        <div class="card-photo p-flock" role="img" aria-label="Flock of ducks flying over a marsh"></div>
        <h4>Wildlife Photography</h4>
        <p>How to follow a moving flock without losing focus.</p>
        <div class="date">May 18, 2024</div>
      </article>
      <article class="card">
        <div class="card-photo p-ducks" role="img" aria-label="Pair of ducks on deep blue water"></div>
        <h4>Wildlife Photography</h4>
        <p>Reading water and light for calm, clean reflections.</p>
        <div class="date">May 2, 2024</div>
      </article>
    </div>
  </section>

  <footer class="footer">
    <div class="footer-cols">
      <div class="footer-col footer-about">
        <h5>WILD PHOTOGRAPHY</h5>
        <p>Outdoor wildlife photography by Nora Falkett, available for editorial work, assignments and print sales across the country.</p>
        <div class="social"><span></span><span></span><span></span><span></span></div>
      </div>
      <div class="footer-col links">
        <h5>ABOUT US</h5>
        <ul><li>Our Story</li><li>Awards Won</li><li>Gallery</li><li>Articles</li></ul>
      </div>
      <div class="footer-col links">
        <h5>QUICK LINKS</h5>
        <ul><li>Portfolio</li><li>Workshops</li><li>Fine Art Prints</li><li>Fan Corner</li></ul>
      </div>
      <div class="footer-col contact">
        <h5>CONTACT US</h5>
        <ul>
          <li><svg viewBox="0 0 12 12"><path d="M6 1a3.5 3.5 0 0 0-3.5 3.5C2.5 7.5 6 11 6 11s3.5-3.5 3.5-6.5A3.5 3.5 0 0 0 6 1zm0 4.8a1.3 1.3 0 1 1 0-2.6 1.3 1.3 0 0 1 0 2.6z" fill="#bdbdbd"/></svg>4817 Maple Hollow Lane, Columbia MD 21078</li>
          <li><svg viewBox="0 0 12 12"><path d="M3 1l2 2.5-1.2 1.2a6 6 0 0 0 3.5 3.5L8.5 7 11 9l-1.5 2C5 11 1 7 1 2.5z" fill="#bdbdbd"/></svg>443-581-2094</li>
          <li><svg viewBox="0 0 12 12"><rect x="1" y="2.5" width="10" height="7" fill="none" stroke="#bdbdbd"/><path d="M1 2.5l5 4 5-4" fill="none" stroke="#bdbdbd"/></svg>Nora@FernOwlPix.com</li>
        </ul>
      </div>
    </div>
    <div class="copyright">© 2024 Wild Photography. All rights reserved.</div>
  </footer>

</div>
</body>
</html>
```